Dane Calloway Photography

Would like the Business card to have a cool logo. I’m targeting wedding/ engagement: portrait photography. My phone number on it. And my business email address.

Target Market(s)

Wedding/portrait/engagement photography.

```html
<!DOCTYPE html>
<html lang="en">
<head>
<meta charset="utf-8">
<title>Dane Calloway Photography — Business Card</title>
<link href="https://fonts.googleapis.com/css2?family=Montserrat:wght@300;400&display=swap" rel="stylesheet">
<style>
  :root {
    --backdrop: #1b1b1d;
    --card: #0d0d0e;
    --gold: #c9a464;
    --gold-soft: #b38e52;
  }
  * { margin: 0; padding: 0; box-sizing: border-box; }
  html, body {
    width: 896px;
    height: 1200px;
    overflow: hidden;
    background: var(--backdrop);
    font-family: "Montserrat", Arial, sans-serif;
  }
  .sheet {
    width: 896px;
    height: 1200px;
    display: flex;
    flex-direction: column;
    align-items: center;
    justify-content: center;
    gap: 110px;
  }
  .card {
    width: 700px;
    height: 400px;
    background: var(--card);
    color: var(--gold);
    display: flex;
    flex-direction: column;
    align-items: center;
    justify-content: center;
    box-shadow: 0 18px 40px rgba(0, 0, 0, 0.55);
  }
  .brand-seal {
    width: 250px;
    height: 250px;
    border: 1.5px solid var(--gold);
    border-radius: 50%;
    display: flex;
    align-items: center;
    justify-content: center;
    text-align: center;
  }
  .brand-seal__name {
    font-weight: 400;
    font-size: 15px;
    letter-spacing: 3px;
    line-height: 1.8;
    text-transform: uppercase;
    color: var(--gold);
    padding-left: 3px;
  }
  .studio-name {
    font-weight: 400;
    font-size: 30px;
    letter-spacing: 6px;
    text-transform: uppercase;
    padding-left: 6px;
    margin-top: 20px;
  }
  .studio-tagline {
    font-weight: 300;
    font-size: 12px;
    letter-spacing: 7px;
    text-transform: uppercase;
    padding-left: 7px;
    margin-top: 8px;
    color: var(--gold-soft);
  }
  .contact-list {
    list-style: none;
    margin-top: 32px;
    font-weight: 300;
    font-size: 11px;
    letter-spacing: 1.5px;
    line-height: 1.9;
    color: var(--gold-soft);
  }
  .contact-item {
    display: flex;
    align-items: center;
    gap: 8px;
  }
  .contact-icon { width: 10px; height: 10px; }
</style>
</head>
<body>
  <main class="sheet">
    <section class="card card--front" aria-label="Card front">
      <div class="brand-seal">
        <p class="brand-seal__name">Dane Calloway<br>Photography</p>
      </div>
    </section>

    <section class="card card--back" aria-label="Card back">
      <h1 class="studio-name">Dane Calloway</h1>
      <p class="studio-tagline">Photography</p>
      <ul class="contact-list">
        <li class="contact-item">
          <svg class="contact-icon" viewBox="0 0 24 24" aria-hidden="true"><path fill="var(--gold-soft)" d="M6.6 10.8a15.1 15.1 0 0 0 6.6 6.6l2.2-2.2a1 1 0 0 1 1-.25 11.4 11.4 0 0 0 3.6.57 1 1 0 0 1 1 1V20a1 1 0 0 1-1 1A17 17 0 0 1 3 4a1 1 0 0 1 1-1h3.5a1 1 0 0 1 1 1c0 1.25.2 2.45.57 3.57a1 1 0 0 1-.25 1z"/></svg>
          <span>+1 (555) 014 7823</span>
        </li>
        <li class="contact-item">
          <svg class="contact-icon" viewBox="0 0 24 24" aria-hidden="true"><rect x="2" y="5" width="20" height="14" fill="none" stroke="var(--gold-soft)" stroke-width="2"/><path d="M2 6l10 7 10-7" fill="none" stroke="var(--gold-soft)" stroke-width="2"/></svg>
          <span>hello@danecalloway.com</span>
        </li>
      </ul>
    </section>
  </main>
</body>
</html>
```